ZEPHIRO needs a new business card!

ZEPHIRO is a group of gaming enthusiasts who are looking for a new corporate business card.

The typeface should be modern and minimalist with attention paid to spacing between the letters and the letters 'zephiro' look relative to each other.

Should clean, crisp and minimalist - looking serious overall but with slight tweaks to the letters to make them look playful...

Black on white is fine.

Details on the card should include:
-the word 'zephiro'
-a job title (use any, for e.g. founder)
-a name (e.g. Ned Falka)
-phone number
-email address

For inspiration: http://brisket.tumblevane-cdn.example/wp-content/uploads/2013/07/mela-1.jpg

Target Market(s)

Video gaming enthusiasts

Industry/Entity Type

Business

Requirements
Must have
• Black letter on white background.
The word "zephiro"
Nice to have
• Maybe use a conservative font like Gibraltar or Helvetica and tweaking each letter individually.

You can insert normal job titles under the "zephiro" typeface
Should not have
• Should not be cartoony or childish fonts. No colors.

```html
<!DOCTYPE html>
<html lang="en">
<head>
<meta charset="utf-8">
<title>ZEPHIRO business card</title>
<link rel="stylesheet" href="https://fonts.googleapis.com/css2?family=Lato:wght@400;700&display=swap">
<style>
  :root {
    --ink: #000000;
    --paper: #ffffff;
    --backdrop: #e8e6e3;
    --card-shadow: rgba(0, 0, 0, 0.28);
  }
  * { box-sizing: border-box; margin: 0; padding: 0; }
  html, body {
    width: 1200px;
    height: 1000px;
    overflow: hidden;
  }
  body {
    background: var(--backdrop);
    font-family: "Lato", Arial, sans-serif;
    position: relative;
  }
  .card {
    position: absolute;
    top: 350px;
    width: 536px;
    height: 300px;
    border-radius: 9px;
    box-shadow: 3px 5px 10px var(--card-shadow);
    overflow: hidden;
  }
  .card--front { left: 46px; background: var(--paper); color: var(--ink); }
  .card--back  { left: 617px; background: var(--ink); color: var(--paper); }

  .wordmark {
    position: absolute;
    font-weight: 400;
    line-height: 1;
    letter-spacing: 1px;
  }
  .card--front .wordmark {
    left: 46px;
    top: 60px;
    font-size: 62px;
  }
  .card--back .wordmark {
    left: 0;
    right: 0;
    top: 108px;
    text-align: center;
    font-size: 70px;
  }

  .holder {
    position: absolute;
    right: 56px;
    top: 74px;
    text-align: left;
  }
  .holder__name {
    font-size: 28px;
    font-weight: 700;
    line-height: 1;
    letter-spacing: -0.2px;
  }
  .holder__title {
    font-size: 21px;
    font-weight: 400;
    letter-spacing: 5px;
    line-height: 1;
    margin-top: 6px;
  }

  .contact-band {
    position: absolute;
    left: 0;
    right: 0;
    top: 207px;
    height: 33px;
    background: var(--ink);
    color: var(--paper);
    display: flex;
    justify-content: space-between;
    align-items: center;
    padding: 0 56px 0 48px;
    font-size: 18px;
    font-weight: 700;
    letter-spacing: 0.3px;
  }
</style>
</head>
<body>
  <section class="card card--front" aria-label="Card front">
    <div class="wordmark">zephiro</div>
    <div class="holder">
      <div class="holder__name">Ned Falka</div>
      <div class="holder__title">founder</div>
    </div>
    <div class="contact-band">
      <span class="contact-band__phone">0147 258 369</span>
      <span class="contact-band__email">ned.falka@zephiro.com</span>
    </div>
  </section>

  <section class="card card--back" aria-label="Card back">
    <div class="wordmark">zephiro</div>
  </section>
</body>
</html>
```